会社の名刺デザインを新しくしたいと思っています。シンプルで明るい印象を与えるデザインを希望します。名刺の背景は白地でお願いします。

ロゴデータを添付しますので、ロゴを生かしたデザインでお願いいたします。

表面にはキャッチコピー「未来を照らすものづくり」を入れてください。(ものづくりを強調してください。)
(例)
表面:会社名/役職/氏名(日本語・英語)/住所/電話/Fax/Mail/キャッチコピー

サンプルは 森川健二(Morikawa Kenji)の名前でお願いします。
会社のURLはこちらです。

http://rbu.co.jp/page2.html#eco

■納品希望形式

イラストレーター形式(当方、Adobe Illustrator CS2です)

名刺デザインですので、氏名等を変更するので、
フォントのアウトライン化はしないでください。

こちらで印刷する予定なので、カラーモード(CMYK)、仕上がりサイズ、画像の埋め込みなど必ずご確認ください。

http://kspprint.net/guide-item.html

宜しくお願いします。

ロゴの画像のみ使っていただいて、会社名のデザインやフォントは変更していただいて構いません。

締め切りまで時間がなくて申し訳ないのですが、もうすこし自由な発想でデザインいただければ幸いです。

エコのイメージをわかりやすくシンプルに表現していただけたので、こちらのデザインに決めさせていただきました。可愛くなりすぎず、固くなりすぎず、丁度よいバランスでとても気に入っています。ありがとうございました。

短い期間でしたが沢山の方にご応募いただきありがとうございました。
おかげ様で納得のいくデザインを選ぶことができました。
また、何かありましたら宜しくお願いします。

```html
<!DOCTYPE html>
<html lang="ja">
<head>
<meta charset="utf-8">
<title>RBU 株式会社 名刺</title>
<link rel="stylesheet" href="https://fonts.googleapis.com/css2?family=Noto+Sans+JP:wght@400;500;700&display=swap">
<style>
  :root {
    --green: #7dc242;
    --green-deep: #5fae2e;
    --green-pale: #e9f4df;
    --ink: #222222;
    --grey: #666666;
    --paper: #ffffff;
  }
  * { margin: 0; padding: 0; box-sizing: border-box; }
  html, body { width: 726px; height: 1200px; overflow: hidden; background: var(--paper); }
  body { font-family: "Noto Sans JP", sans-serif; color: var(--ink); }
  .card { position: relative; width: 726px; height: 1200px; background: var(--paper); overflow: hidden; }

  .brand-mark { position: absolute; left: 78px; top: 44px; width: 140px; height: 140px; border-radius: 50%; background: var(--green); }
  .brand-name { position: absolute; left: 244px; top: 52px; font-size: 46px; font-weight: 700; letter-spacing: 4px; color: var(--ink); line-height: 1; }
  .brand-rule { position: absolute; left: 244px; top: 114px; width: 400px; height: 3px; background: var(--ink); }
  .brand-en { position: absolute; left: 246px; top: 122px; font-size: 25px; color: var(--ink); line-height: 1.2; }

  .person { position: absolute; left: 0; width: 726px; text-align: center; }
  .role { top: 350px; font-size: 27px; letter-spacing: 10px; color: var(--grey); }
  .name { top: 390px; font-size: 60px; font-weight: 700; letter-spacing: 2px; line-height: 1.2; }
  .name .accent { color: var(--green); }
  .name-en { top: 484px; font-size: 25px; color: var(--grey); }

  .contacts { position: absolute; left: 340px; top: 540px; list-style: none; }
  .contacts li { display: flex; align-items: center; height: 50px; font-size: 27px; color: var(--grey); }
  .contacts svg { width: 28px; height: 28px; margin-right: 12px; }

  .halo { position: absolute; left: 253px; top: 713px; width: 220px; height: 220px; border-radius: 50%; background: var(--green-pale); opacity: 0.55; }

  .tagline { position: absolute; left: 150px; top: 902px; font-size: 31px; color: var(--grey); }
  .tagline strong { font-size: 39px; font-weight: 700; color: var(--green); }

  .footer-company { position: absolute; left: 78px; top: 968px; font-size: 37px; font-weight: 700; white-space: nowrap; }
  .footer-company span { font-size: 25px; font-weight: 400; margin-left: 10px; }

  .address { position: absolute; left: 100px; top: 1035px; font-size: 33px; color: var(--ink); white-space: nowrap; }
  .address small { font-size: 24px; margin-right: 10px; }

  .lines { position: absolute; left: 94px; top: 1095px; display: flex; gap: 30px; font-size: 35px; color: var(--ink); }
  .lines div { display: flex; align-items: center; }
  .lines svg { width: 34px; height: 34px; margin-right: 6px; }

  .band { position: absolute; left: 0; bottom: 0; width: 726px; height: 40px; background: linear-gradient(90deg, #a9d67f, var(--green-deep)); }
</style>
</head>
<body>
<div class="card">
  <div class="brand-mark" aria-hidden="true"></div>
  <div class="brand-name">RBU 株式会社</div>
  <div class="brand-rule"></div>
  <div class="brand-en">Riverbend Utility Co., Ltd.</div>

  <p class="person role">役職</p>
  <p class="person name"><span class="accent">森</span>川 健二</p>
  <p class="person name-en">Morikawa Kenji</p>

  <ul class="contacts">
    <li><svg viewBox="0 0 24 24"><rect x="7" y="2" width="10" height="20" rx="2" fill="none" stroke="var(--green)" stroke-width="2"/><rect x="9" y="5" width="6" height="8" fill="var(--green)"/></svg>000-0000-0000</li>
    <li><svg viewBox="0 0 24 24"><rect x="2" y="5" width="20" height="14" fill="none" stroke="var(--green)" stroke-width="2"/><path d="M2 5l10 8 10-8" fill="none" stroke="var(--green)" stroke-width="2"/></svg>morikawa@rbu.co.jp</li>
  </ul>

  <div class="halo" aria-hidden="true"></div>

  <p class="tagline">未来を照らす<strong>ものづくり</strong></p>
  <p class="footer-company">RBU 株式会社<span>Riverbend Utility Co., Ltd.</span></p>
  <p class="address"><small>〒000-0000</small>●●●県●●市●●000</p>
  <div class="lines">
    <div><svg viewBox="0 0 24 24"><path d="M6 2c2 0 3 4 3 5s-2 2-2 3 3 6 5 7c1 0 2-2 3-2s5 1 5 3-2 4-4 4C9 22 2 15 2 6c0-2 2-4 4-4z" fill="var(--green)"/></svg>0000-00-0000</div>
    <div><svg viewBox="0 0 24 24"><rect x="6" y="2" width="12" height="6" fill="none" stroke="var(--green)" stroke-width="2"/><rect x="2" y="8" width="20" height="10" rx="2" fill="var(--green)"/><rect x="6" y="14" width="12" height="8" fill="#fff" stroke="var(--green)" stroke-width="2"/></svg>0000-00-0000</div>
  </div>

  <div class="band"></div>
</div>
</body>
</html>
```